movie poster for a bittersweet romantic drama

Hello everyone. Looking for a dynamic poster for feature film 'Mabel's Harbor' a romantic drama. It is a bittersweet love story so not rosey lovie dovie type.

300dpi

Please visit the link below for the poster image
https://www.filevault-example.net/s/k8p2r41xqz7mv5b/_Q7T4416.tif?dl=0

poster should have:
1. title of film : Mabel's Harbor
2. tagline of film:
Death knows no names
Love does not know race

3. A film by Lucinda P. Okwemba
4 Include the logo for 'Teruvo Films' attached below

poster size:
1. 8x10
2. thumnail
3. landscape with just film title
4. 27 by 41

Target Market(s)

15-55 men and mostly women

Industry/Entity Type

Film Production

Colors

Designer to choose colors to be used in the design.

Requirements
Must have
• Dynamic and vibrant
• it is a romantic drama so love on a serious note
Nice to have
• Play with romantic fonts but don't overdo it.
Should not have
• must not look like a romance novel

```html
<!DOCTYPE html>
<html lang="en">
<head>
<meta charset="utf-8">
<title>Mabel's Harbor — Landscape Title Poster</title>
<link rel="stylesheet" href="https://fonts.googleapis.com/css2?family=Bodoni+Moda:opsz,wght@6..96,500&family=Lato:wght@400;700&display=swap">
<style>
  :root {
    --backdrop: #e4e3e0;
    --paper: #ffffff;
    --ink: #1a1414;
    --title-red: #c1141f;
    --title-dark: #1c0d0e;
    --rule: #b0151e;
  }
  html, body {
    margin: 0;
    padding: 0;
    width: 1200px;
    height: 1148px;
    overflow: hidden;
    background: var(--backdrop);
  }
  .poster {
    position: absolute;
    left: 40px;
    top: 201px;
    width: 1120px;
    height: 746px;
    background: var(--paper);
    box-shadow: 0 2px 14px rgba(0,0,0,0.12);
  }
  .poster__title {
    position: absolute;
    left: 0;
    top: 0;
    width: 1120px;
    height: 746px;
  }
  .poster__title text {
    font-family: "Bodoni Moda", "Didot", serif;
    font-weight: 500;
    font-size: 108px;
  }
  .tagline {
    position: absolute;
    left: 639px;
    top: 452px;
    font-family: "Lato", Arial, sans-serif;
    color: var(--ink);
    text-transform: uppercase;
    line-height: 1.2;
  }
  .tagline__lead { font-size: 13px; letter-spacing: 0.02em; }
  .tagline__main { font-size: 18px; letter-spacing: 0.02em; }
  .credit {
    position: absolute;
    left: 655px;
    top: 640px;
    display: flex;
    align-items: center;
    font-family: "Lato", Arial, sans-serif;
    color: var(--ink);
  }
  .studio {
    display: flex;
    align-items: center;
    gap: 6px;
    font-size: 14px;
    font-weight: 700;
    text-transform: uppercase;
  }
  .studio__mark {
    width: 10px;
    height: 10px;
    background: var(--ink);
  }
  .credit__rule {
    width: 2px;
    height: 26px;
    background: var(--rule);
    margin: 0 8px 0 10px;
  }
  .director { text-transform: uppercase; line-height: 1.15; }
  .director__label { font-size: 9px; }
  .director__name { font-size: 13px; }
</style>
</head>
<body>
  <main class="poster">
    <svg class="poster__title" viewBox="0 0 1120 746" aria-label="Mabel's Harbor">
      <defs>
        <linearGradient id="title-fill" x1="0" y1="0" x2="0" y2="1">
          <stop offset="0" stop-color="var(--title-red)"/>
          <stop offset="0.45" stop-color="#a01119"/>
          <stop offset="1" stop-color="var(--title-dark)"/>
        </linearGradient>
      </defs>
      <text x="560" y="433" text-anchor="middle" textLength="880" lengthAdjust="spacingAndGlyphs" fill="url(#title-fill)">MABEL'S HARBOR</text>
    </svg>

    <div class="tagline">
      <div class="tagline__lead">Death knows no names</div>
      <div class="tagline__main">Love does not know race</div>
    </div>

    <div class="credit">
      <div class="studio"><span class="studio__mark"></span>Teruvo Films</div>
      <div class="credit__rule"></div>
      <div class="director">
        <div class="director__label">A film by</div>
        <div class="director__name">Lucinda P. Okwemba</div>
      </div>
    </div>
  </main>
</body>
</html>
```